Plumbing Company After Business Card

Business card for a plumbing business that offers a variety of plumbing services including maintenance, domestic and commercial plumbing. My main focus is to offer high quality professional service. A logo on the card would be ideal. Any other questions feel free to email. Cheers

Looking for something modern and upmarket with preferably a matte black background

Business name is Crestline Plumbing and Gas

Industry/Entity Type

Plumbing

Contact Information for Business Card

Crestline Plumbing and Gas
Marcus Thorvale
0472519306
14 Karrabee Drive, Ascot 3550
crestlineplumbing@mailbay.com.au
ABN 64 915 207 338

Font styles to use
Sans Serif

Colors
1b1b1b
ffffff
3377b5

Requirements
Must have
• Domestic
• Commercial
• Maintenance

```html
<!DOCTYPE html>
<html lang="en">
<head>
<meta charset="utf-8">
<title>Crestline Plumbing and Gas – Business Card</title>
<link rel="stylesheet" href="https://fonts.googleapis.com/css2?family=Open+Sans:wght@400;600;700&display=swap">
<style>
  :root {
    --canvas-bg: #dfe2e5;
    --card-light: #f3f3f3;
    --card-blue: #1c95d2;
    --brand-blue: #3377b5;
    --ink-dark: #1b1b1b;
    --ink-light: #ffffff;
  }
  * { margin: 0; padding: 0; box-sizing: border-box; }
  html, body {
    width: 1200px;
    height: 900px;
    overflow: hidden;
    background: var(--canvas-bg);
    font-family: "Open Sans", Arial, sans-serif;
  }
  .business-card {
    position: absolute;
    left: 300px;
    top: 213px;
    width: 618px;
    height: 383px;
    display: flex;
    box-shadow: 0 6px 18px rgba(0,0,0,0.12);
  }
  .card-brand {
    width: 309px;
    height: 100%;
    background: var(--card-light);
    display: flex;
    flex-direction: column;
    align-items: center;
    padding-top: 104px;
  }
  .brand-mark {
    width: 120px;
    height: 120px;
    border-radius: 50%;
    background: var(--brand-blue);
  }
  .brand-name {
    margin-top: 16px;
    font-size: 16.5px;
    font-weight: 600;
    color: var(--brand-blue);
    letter-spacing: 0.2px;
    white-space: nowrap;
  }
  .brand-services {
    margin-top: 4px;
    font-size: 14px;
    font-weight: 400;
    color: var(--ink-dark);
    white-space: nowrap;
  }
  .card-contact {
    width: 309px;
    height: 100%;
    background: var(--card-blue);
    color: var(--ink-light);
    padding: 104px 0 0 18px;
  }
  .contact-name {
    font-size: 20px;
    font-weight: 700;
    line-height: 1;
    margin-bottom: 34px;
  }
  .contact-line {
    font-size: 16px;
    line-height: 1;
    margin-bottom: 23px;
  }
  .contact-line.with-icon {
    display: flex;
    align-items: center;
    gap: 9px;
    margin-bottom: 7px;
  }
  .contact-line.address { margin-bottom: 17px; }
  .contact-icon { width: 13px; height: 13px; flex: none; }
</style>
</head>
<body>
  <div class="business-card">
    <section class="card-brand">
      <div class="brand-mark"></div>
      <div class="brand-name">CRESTLINE PLUMBING AND GAS</div>
      <div class="brand-services">Domestic | Commercial | Maintenance</div>
    </section>
    <section class="card-contact">
      <div class="contact-name">Marcus Thorvale</div>
      <div class="contact-line">ABN: 64 915 207 338</div>
      <div class="contact-line address">14 Karrabee Drive, Ascot 3550</div>
      <div class="contact-line with-icon">
        <svg class="contact-icon" viewBox="0 0 24 24" aria-hidden="true">
          <path fill="currentColor" d="M6.6 10.8a15.1 15.1 0 0 0 6.6 6.6l2.2-2.2c.3-.3.7-.4 1-.2 1.1.4 2.3.6 3.6.6.6 0 1 .4 1 1V20c0 .6-.4 1-1 1A17 17 0 0 1 3 4c0-.6.4-1 1-1h3.5c.6 0 1 .4 1 1 0 1.3.2 2.5.6 3.6.1.3 0 .7-.2 1z"/>
        </svg>
        <span>0472519306</span>
      </div>
      <div class="contact-line with-icon">
        <svg class="contact-icon" viewBox="0 0 24 24" aria-hidden="true">
          <rect x="2" y="5" width="20" height="14" rx="1" fill="currentColor"/>
          <path d="M3 6l9 7 9-7" fill="none" stroke="#1c95d2" stroke-width="1.8"/>
        </svg>
        <span>crestlineplumbing@mailbay.com.au</span>
      </div>
    </section>
  </div>
</body>
</html>
```